Bionic Knee Brace Company Needs Brochure Design

Our revolutionary bionic knee braces do more than just stabilize your knee. Quorvanta's™ bionic hinge enhances your leg muscle power by storing energy as you bend your knee and returning that energy as you straighten your leg. The result is the world’s only compact and powerful bionic knee brace capable of boosting strength, mobility, and performance.

We need a double sided one page patient resource made for topics such as ACL injury treatment, osteoarthritis pre-operative care, and osteoarthritis post-operative care.

We are looking for designs that are broadly consistent with the look and feel of our website, product one pager, eBook and other resources. The copy for three different resources are included as attachments.

Please refer to our website for more information about our company and brand: https://brindlecoremedical.example/
Updates

Font styles to use
Sans Serif

Colors
0355a3
0492cd

Requirements
Must have
• -One pagers must be created using Adobe InDesign. The final deliverable is the .indd file.
• -Width: 8.5 in, Height: 11 in
• -Intent: print/web
• -Orientation: portrait
• -Number of pages: 2
• Proxima Nova is the official font of Brindle Core Medical
• The official blue (including in the logo) for Brindle Core Medical is #2075c0.
• Brindle Core Medical has a secondary color, which is dark blue.
• The official dark blue for Brindle Core Medical is # 195a94.
• Brindle Core Medical has a tertiary color, which is yellow.
• The official yellow for Brindle Core Medical is # ffb218.
• Brindle Core Medical has a quaternary color, which is dark grey.
• The official dark grey for Brindle Core Medical is #4c4c4c.
Nice to have
• Ideally, the one pager would be easily changed to accommodate different copy for different resources.

```html
<!DOCTYPE html>
<html lang="en">
<head>
<meta charset="utf-8">
<title>Patient Resource – ACL Injuries</title>
<link href="https://fonts.googleapis.com/css2?family=Bebas+Neue&family=Arimo:wght@400;700&display=swap" rel="stylesheet">
<style>
:root{
  --mat:#000;
  --paper:#fff;
  --ink:#1a1a1a;
  --teal-deep:#137da3;
  --teal:#1a8fb8;
  --teal-light:#2aa9cf;
  --logo-blue:#2075c0;
  --box-deep:#145f7e;
  --box-light:#1e89ae;
}
*{margin:0;padding:0;box-sizing:border-box}
html,body{width:999px;height:1200px;overflow:hidden;background:var(--mat)}
.canvas{position:relative;width:999px;height:1200px;background:var(--mat);font-family:"Arimo",Arial,sans-serif;color:var(--ink)}
.page{position:absolute;left:83px;top:65px;width:845px;height:1090px;background:var(--paper);overflow:hidden}
.brand{position:absolute;left:182px;top:40px;display:flex;align-items:center;gap:14px}
.brand-mark{width:66px;height:66px;background:var(--logo-blue);flex:none}
.brand-name{font-family:"Arimo",Arial,sans-serif;font-weight:700;font-size:29px;line-height:32px;color:var(--logo-blue);letter-spacing:2px}
.hero{position:absolute;left:0;top:143px;width:845px;height:222px;background:linear-gradient(90deg,var(--teal-deep),var(--teal) 55%,var(--teal-light))}
.hero-title{position:absolute;left:40px;top:14px;font-family:"Bebas Neue",Impact,sans-serif;font-weight:400;font-size:95px;line-height:1;color:#fff;letter-spacing:1px;white-space:nowrap}
.hero-topic{position:absolute;left:42px;top:108px;font-weight:700;font-size:30px;color:#fff}
.hero-credit{position:absolute;left:44px;top:153px;font-size:21px;color:#fff}
.product-photo{position:absolute;left:615px;top:32px;width:220px;height:425px;border-radius:30px;background:linear-gradient(180deg,#2a2a2a,#111 60%,#1e2a33)}
.knee-illustration{position:absolute;left:585px;top:495px;width:210px;height:250px;border-radius:8px;background:linear-gradient(180deg,#cfe3f0,#e9d2b6 55%,#ddc09c)}
.content{position:absolute;left:42px;font-size:13px;line-height:1.3}
h2{font-size:17px;font-weight:700}
h3{font-size:15px;font-weight:700}
.list{list-style:none}
.list li{position:relative;padding-left:50px}
.list li::before{content:"•";position:absolute;left:0}
.num{display:inline-block;width:48px}
.two-col{display:flex;gap:45px}
.note{font-size:12px;line-height:1.25}
.factors{position:absolute;left:431px;top:923px;width:392px;height:113px;border-radius:8px;background:linear-gradient(90deg,var(--box-deep),var(--box-light));color:#fff;font-weight:700;font-size:18.5px;line-height:23.5px;padding:12px 14px;white-space:nowrap}
.footer{position:absolute;left:0;top:1050px;width:845px;height:40px;background:linear-gradient(90deg,var(--box-deep),var(--teal-light));color:#fff;font-size:12px;font-weight:700;letter-spacing:4px;text-align:center;line-height:40px}
</style>
</head>
<body>
<div class="canvas">
  <div class="page">
    <div class="brand"><span class="brand-mark"></span><span class="brand-name">BRINDLE CORE<br>MEDICAL</span></div>

    <div class="hero">
      <div class="hero-title">PATIENT RESOURCE</div>
      <div class="hero-topic">–ACL Injuries</div>
      <div class="hero-credit">Information prepared by Daniel Orsett</div>
    </div>
    <div class="product-photo" role="img" aria-label="Product photo of a black bionic knee brace with blue hinge"></div>

    <section class="content" style="top:376px;width:560px">
      <h2>Anatomy of the Knee Joint1,3</h2>
      <ul class="list" style="margin-top:8px">
        <li>Thighbone, shinbone and kneecap form the knee joint</li>
        <li>The bones are connected by 4 main ligaments:</li>
      </ul>
      <h3 style="margin-top:14px">Collateral Ligaments:</h3>
      <p style="margin-top:9px">These ligaments stabilize against side-to-side motion of the knee.</p>
      <p style="margin-top:14px"><span class="num">1)</span><b>Medial Collateral Ligament (MCL)</b> - Inside of the knee</p>
      <p><span class="num">2)</span><b>Lateral Collateral Ligament (LCL)</b> - Outside of the knee</p>
      <h3 style="margin-top:12px">Cruciate Ligaments:</h3>
      <p style="margin-top:9px;width:405px;text-align:justify">These ligaments are inside the joint and cross each other, forming an ‘x’. As a result, these ligaments are able to stabilize against excessive forwards and backwards motion of the knee.</p>
      <p style="margin-top:14px"><span class="num">3)</span><b>Anterior Cruciate Ligament</b> – Attached from the<br>front of the shinbone to the back of the thighbone.</p>
      <p><span class="num">4)</span><b>Posterior Cruciate Ligament</b> – Attached from the<br>back of the shinbone to the front of the thighbone.</p>
      <h2 style="margin-top:18px">The Anterior Cruciate Ligament (ACL)1,2,4</h2>
      <p style="margin-top:9px">Primary Function: To prevent the shinbone from excessive forward movement.</p>
      <div class="two-col" style="margin-top:14px">
        <div style="width:254px">
          <h3>Causes:</h3>
          <ul class="list" style="margin-top:8px">
            <li>Sudden change in direction*</li>
            <li>Abrupt stop or slowing down*</li>
            <li>Improper landing from a jump*</li>
            <li>Direct contact or collision</li>
          </ul>
        </div>
        <div>
          <h3>Symptoms:</h3>
          <p style="margin-top:8px">Pain and Swelling<br>Apparent instability of the knee joint<br>Tenderness in and around the knee<br>Inability or discomfort while walking</p>
        </div>
      </div>
      <p class="note" style="margin-top:10px;width:330px">*Non-Contact injuries (injuries that do not occur from direct contact or a blow to the knee joint) account for 70-80% of all ACL injuries2</p>
      <p style="margin-top:24px;width:320px">Studies show that teenage and adult females may be 2-8x more likely to experience a non-contact ACL injury compared to males for a variety of proposed differences2,4:</p>
    </section>

    <div class="knee-illustration" role="img" aria-label="Illustration of the knee joint with labelled femur, patella, tibia, fibula and the four ligaments"></div>

    <div class="factors">Muscular strength<br>Neuromuscular coordination and control<br>Pelvic and leg alignment<br>Hormones</div>

    <div class="footer">brindlecoremedical.example</div>
  </div>
</div>
</body>
</html>
```